Need a Facebook image for childcare advertisement

We are after a design for Facebook advertisement for childcare and kindergarten centre enrolments for 2023.

I have attached a previous flyer that we have in pdf format. The new logo is also attached with this brief.

All other information is still current as per the attached flyer.

You can use same colours as per attached flyer. I will also attached some stock images that you can select to use for the design.

our website for your reference:

https://tolvenbrook.com.au

```html
<!DOCTYPE html>
<html lang="en">
<head>
<meta charset="utf-8">
<title>Tolvenbrook Early Childhood Learning Centre – Book a Tour</title>
<link rel="stylesheet" href="https://fonts.googleapis.com/css2?family=Baloo+2:wght@700;800&family=Poppins:wght@400;500;600&display=swap">
<style>
  :root {
    --sky: #5ec3ea;
    --sunshine: #ffe600;
    --purple-top: #8b2f9c;
    --purple-bottom: #3f3f9e;
    --white: #ffffff;
    --ink: #2a2a3a;
    --logo-red: #e8352b;
  }
  html, body {
    margin: 0;
    width: 1200px;
    height: 1200px;
    overflow: hidden;
    background: var(--sky);
  }
  .canvas {
    position: relative;
    width: 1200px;
    height: 1200px;
    background: var(--sky);
    font-family: "Poppins", sans-serif;
  }
  .artboard {
    position: absolute;
    left: 50px;
    top: 50px;
    width: 1100px;
    height: 1100px;
    overflow: hidden;
    box-shadow: 0 0 18px rgba(0, 40, 80, 0.35);
  }
  .hero-photo {
    position: absolute;
    inset: 0;
    background:
      radial-gradient(ellipse 420px 520px at 830px 360px, #c99a6a 0%, #9a7860 35%, transparent 70%),
      linear-gradient(160deg, #e9e6e2 0%, #cfcbc6 40%, #8a8f97 70%, #5a6270 100%);
  }
  .yellow-band {
    position: absolute;
    left: 0;
    right: 0;
    top: 800px;
    bottom: 0;
    background: var(--sunshine);
  }
  .brand {
    position: absolute;
    left: 62px;
    top: 22px;
    width: 290px;
    text-align: center;
    color: var(--ink);
  }
  .brand-name {
    display: flex;
    align-items: center;
    justify-content: center;
    gap: 10px;
    font-family: "Baloo 2", sans-serif;
    font-weight: 800;
    font-size: 44px;
    line-height: 1;
    color: var(--logo-red);
  }
  .brand-mark {
    width: 22px;
    height: 22px;
    border-radius: 50%;
    background: var(--logo-red);
  }
  .brand-tagline {
    margin-top: 8px;
    font-size: 13px;
    font-weight: 500;
    letter-spacing: 0.2px;
    color: var(--ink);
  }
  .panel {
    position: absolute;
    left: 0;
    top: 0;
  }
  .panel-copy {
    position: absolute;
    left: 78px;
    top: 310px;
    width: 400px;
    color: var(--white);
  }
  .headline {
    margin: 0;
    font-family: "Baloo 2", sans-serif;
    font-weight: 700;
    font-size: 57px;
    line-height: 58px;
  }
  .intro {
    margin: 14px 0 0;
    font-size: 18px;
    line-height: 23px;
  }
  .divider {
    margin: 20px 0 0;
    width: 380px;
    height: 3px;
    background: var(--white);
    border: 0;
  }
  .subheading {
    margin: 16px 0 0;
    font-family: "Baloo 2", sans-serif;
    font-weight: 700;
    font-size: 40px;
    line-height: 45px;
    color: var(--sunshine);
  }
  .contact {
    position: absolute;
    left: 78px;
    top: 948px;
    font-family: "Baloo 2", sans-serif;
    font-weight: 700;
    font-size: 28px;
    line-height: 38px;
  }
  .contact-label { color: var(--sunshine); }
  .contact-phone { color: var(--white); }
  .tour-badge {
    position: absolute;
    left: 372px;
    top: 186px;
    width: 210px;
    height: 170px;
  }
  .tour-badge-text {
    position: absolute;
    left: 390px;
    top: 226px;
    width: 170px;
    transform: rotate(22deg);
    font-family: "Baloo 2", sans-serif;
    font-weight: 800;
    font-size: 34px;
    line-height: 32px;
    color: #3a3a9a;
    text-align: center;
  }
  .snapshot {
    position: absolute;
    border: 9px solid var(--white);
    box-shadow: 0 4px 12px rgba(0, 0, 0, 0.3);
  }
  .snapshot-artwork {
    left: 485px;
    top: 680px;
    width: 270px;
    height: 150px;
    transform: rotate(-6deg);
    background: linear-gradient(135deg, #c9b9c8 0%, #a97f8c 45%, #6d6a86 100%);
  }
  .snapshot-reading {
    left: 450px;
    top: 880px;
    width: 300px;
    height: 185px;
    transform: rotate(-4deg);
    background: linear-gradient(135deg, #d9b9a5 0%, #c78a86 45%, #8a6a62 100%);
  }
  .snapshot-drawing {
    left: 770px;
    top: 735px;
    width: 290px;
    height: 215px;
    transform: rotate(-5deg);
    background: linear-gradient(135deg, #e8d2b4 0%, #e3b6b9 50%, #b9a4a8 100%);
  }
</style>
</head>
<body>
<div class="canvas">
  <div class="artboard">
    <div class="hero-photo" role="img" aria-label="Photo of a young boy drawing with a blue pencil at a classroom table"></div>
    <div class="yellow-band"></div>

    <svg class="panel" width="1100" height="1100" viewBox="0 0 1100 1100" aria-hidden="true">
      <defs>
        <linearGradient id="panelFill" x1="0" y1="0" x2="0" y2="1">
          <stop offset="0" stop-color="var(--purple-top)"/>
          <stop offset="1" stop-color="var(--purple-bottom)"/>
        </linearGradient>
      </defs>
      <path d="M78 172 Q30 172 30 222 L30 1020 Q30 1068 78 1068 L440 1068 Q476 1068 482 1032 L610 220 Q616 172 566 172 Z"
            fill="url(#panelFill)" stroke="var(--white)" stroke-width="9" stroke-linejoin="round"/>
    </svg>

    <div class="brand">
      <div class="brand-name"><span class="brand-mark"></span>Tolvenbrook</div>
      <div class="brand-tagline">EARLY CHILDHOOD LEARNING CENTRE</div>
    </div>

    <svg class="tour-badge" viewBox="0 0 210 170" aria-hidden="true">
      <g transform="rotate(22 105 80)">
        <rect x="20" y="20" width="170" height="110" rx="14" fill="var(--sunshine)"/>
        <path d="M60 125 L52 168 L95 128 Z" fill="var(--sunshine)"/>
      </g>
    </svg>
    <div class="tour-badge-text">BOOK<br>A TOUR</div>

    <div class="panel-copy">
      <h1 class="headline">Spark A Lifelong Love Of Learning In Your Child</h1>
      <p class="intro">Encourage them to explore, play, dis-cover, and just be themselves in a safe, nurturing environment.</p>
      <hr class="divider">
      <p class="subheading">Start Your Child’s Educational Journey The Right Way</p>
    </div>

    <div class="contact">
      <div class="contact-label">FREE Consultation</div>
      <div class="contact-phone">(03) 9400 2716</div>
    </div>

    <div class="snapshot snapshot-artwork" role="img" aria-label="Photo of children holding up their colourful paintings"></div>
    <div class="snapshot snapshot-reading" role="img" aria-label="Photo of a teacher reading with a small group of children"></div>
    <div class="snapshot snapshot-drawing" role="img" aria-label="Photo of two children drawing together at a desk"></div>
  </div>
</div>
</body>
</html>
```